Varlo Intellectual Property Logo & Business card design brief

Dear Sir/Madam,

I need to have a logo design incorporated into a business card layout so as to then have these formatted files available to me to then take to printers for print production. Am I right to believe that this design task from start to finish can be turned around in 5 days and please clarify if these 5 days incorporate the weekend?

Fyi I wish the logo colours to be a bright burnt orange and vivid azure blue like the ocean on a clear day - I have these colours on a JPEG image that I can email the successful tendering / competition wining design party. Additionally I'd like to incorporate a proportionately scaled simplified earth globe orientating towards Australia and SE Asia - showing prominately Southern China. This globe can either be stand alone &/or incorporated into the Varlo brand mark. Some gold colour gilding on say the meridian lines would look striking and distinctive.

Nb - the reverse side of the business card will simply have our Hong Kond office address details in Chinese Characters

Put simply, I want our logo and business card layout to look elegant, classy and classic without being too hip &/or trendy. Although this is a new start up company I want the look and feel to be like an established and venerated brand that sits proudly amongst professional positioned financial groups and organisations which are our cleintele.

Looking forward to working with your organisation to achieve this task and revealing the winner on Monday. For precise guidance purposes I can forward preferred colour palate for final artwork finesse .

Regards Denis - Sales & Marketing Director
Varlo Property Group
Melbourne , Australia

Target Market(s)

Professional investor high net work individuals . Companies and managed investment funds looking to invest into Australian property developments

Industry/Entity Type

Property Management

Contact Information for Business Card

Level 2, 287 Harcourt Ln,
Melbourne, Vic 3004. | Australia

Font styles to use
Serif

Colors
0555a3
f37122

Requirements
Must have
• A professional elegant and classy look and feel to the overall brand mark and type face . Classic fonts over trendy hip styles would be preferred. For guidance purposes look at major global banks and investment companies
Nice to have
• Being a property development group and for positioning purposes we
• Require a assic yet innovative feel here is to achieve the balance
Should not have
• The actual company name and address details can be black on white background , but within the actual logo design & the accompanying globe with the meridian lines please DO NOT use white & black in this component of the brand mark

```html
<!DOCTYPE html>
<html lang="en">
<head>
<meta charset="utf-8">
<title>Varlo Intellectual Property – Business Card</title>
<link href="https://fonts.googleapis.com/css2?family=Alegreya:wght@500&family=Open+Sans:wght@400;600&display=swap" rel="stylesheet">
<style>
  :root {
    --azure: #0555a3;
    --burnt-orange: #f37122;
    --ink: #2b2b2b;
    --ink-dark: #1a1a1a;
    --paper: #ffffff;
    --backdrop: #e9e7e4;
    --portrait-light: #8a8580;
    --portrait-dark: #2a2a2e;
  }
  * { margin: 0; padding: 0; box-sizing: border-box; }
  html, body {
    width: 1200px; height: 900px; overflow: hidden;
    background: var(--backdrop);
  }
  .canvas { position: relative; width: 1200px; height: 900px; }

  .card {
    position: absolute;
    background: var(--paper);
    overflow: hidden;
    box-shadow: 0 6px 18px rgba(0,0,0,0.18);
  }
  .card--front { left: 238px; top: 60px; width: 555px; height: 345px; }
  .card--back  { left: 457px; top: 518px; width: 560px; height: 345px; }

  .front-waves { position: absolute; inset: 0; }

  .portrait {
    position: absolute;
    left: 314px; top: 22px; width: 241px; height: 323px;
    border-radius: 110px 110px 0 0;
    background: linear-gradient(180deg, var(--portrait-light) 0%, #5a544f 35%, var(--portrait-dark) 70%);
  }

  .brand {
    position: absolute; left: 30px; top: 38px;
    color: var(--paper);
    font-family: "Alegreya", Georgia, serif;
    font-weight: 500;
  }
  .brand__name { font-size: 40px; line-height: 1; letter-spacing: 0.5px; }
  .brand__tagline { font-size: 16px; margin-top: 8px; letter-spacing: 0.3px; }

  .contact {
    position: absolute; left: 29px; top: 144px;
    font-family: "Open Sans", Arial, sans-serif;
    color: var(--ink);
    font-size: 14px; line-height: 20px;
  }
  .contact__name { color: var(--burnt-orange); font-weight: 600; font-size: 17px; line-height: 22px; }
  .contact__role { margin-bottom: 14px; }
  .contact__address { margin-bottom: 14px; }
  .contact__line { display: flex; align-items: center; gap: 9px; }
  .contact__line svg { width: 11px; height: 11px; fill: var(--burnt-orange); flex: none; }

  .back-logo {
    position: absolute; left: 0; right: 0; top: 148px;
    text-align: center;
    font-family: "Alegreya", Georgia, serif;
    font-weight: 500;
  }
  .back-logo__name {
    display: inline-flex; align-items: center; gap: 12px;
    color: var(--azure); font-size: 66px; line-height: 1;
  }
  .back-logo__mark { width: 22px; height: 22px; background: var(--burnt-orange); }
  .back-logo__tagline {
    color: var(--ink-dark); font-size: 23px; margin-top: 14px; letter-spacing: 0.4px;
  }
</style>
</head>
<body>
<main class="canvas">

  <section class="card card--front" aria-label="Business card front">
    <svg class="front-waves" viewBox="0 0 555 345" width="555" height="345" aria-hidden="true">
      <path d="M0 0 H555 V150 C520 110 470 70 380 45 C260 14 120 14 0 30 Z" fill="var(--burnt-orange)"/>
      <path d="M0 30 C120 14 260 14 380 45 C470 70 520 110 555 150 V172 C515 128 460 90 370 64 C250 32 120 28 0 40 Z" fill="var(--paper)"/>
      <path d="M0 40 C120 28 250 32 370 64 C460 90 515 128 555 172 V220 C430 175 300 160 160 140 C100 132 45 124 0 116 Z" fill="var(--azure)"/>
    </svg>

    <div class="portrait" role="img" aria-label="Portrait photograph of the sales and marketing director in a dark suit"></div>

    <div class="brand">
      <div class="brand__name">Varlo</div>
      <div class="brand__tagline">Intellectual Property</div>
    </div>

    <div class="contact">
      <div class="contact__name">Denis</div>
      <div class="contact__role">Sales &amp; Marketing Director</div>
      <div class="contact__address">Level 2, 287 Harcourt Ln,<br>Melbourne, Vic 3004. | Australia</div>
      <div class="contact__line">
        <svg viewBox="0 0 12 12"><path d="M2.4 0.6 L4.3 2.6 L3.3 4.1 C4 5.7 6.3 8 7.9 8.7 L9.4 7.7 L11.4 9.6 L10 11.4 C5.6 11 1 6.4 0.6 2 Z"/></svg>
        <span>041-785 302 146</span>
      </div>
      <div class="contact__line">
        <svg viewBox="0 0 12 12"><path d="M0 2 H12 V3 L6 6.6 L0 3 Z M0 4.4 L6 8 L12 4.4 V10 H0 Z"/></svg>
        <span>hello@varlomail.com</span>
      </div>
      <div class="contact__line">
        <svg viewBox="0 0 12 12"><circle cx="6" cy="6" r="6"/><path d="M3 3.5 C4.5 3 5 4.5 4 5.5 C3.5 6.5 5 7 4.5 9 M8 2.5 C7 4 9 4.5 9.5 6" stroke="var(--paper)" stroke-width="1" fill="none"/></svg>
        <span>www.varloproperty.com</span>
      </div>
    </div>
  </section>

  <section class="card card--back" aria-label="Business card back">
    <div class="back-logo">
      <div class="back-logo__name"><span class="back-logo__mark"></span>Varlo</div>
      <div class="back-logo__tagline">Intellectual Property</div>
    </div>
  </section>

</main>
</body>
</html>
```